Research and Innovation programme/projects in WOOD based industries

1.Trnavska s.r.o. (offical registered brand name of our company)
-Managing technology development projects
-International cooperation and development European projects
Our company was founded in 2008 and started to work as a counsilary company operating in the section of european funds administrated by Czech republic. Nowadays we are specializing on projects in the sphere of science and research co-financed by EU.Since 6.6.2013 we are registered under European comission for a purpose of broad support of transnational projects.

Target Market(s)

We are primarily focused on european companies, which stand behind the latest research and innovation of sawing, planing, glulam and logging technologies based on wooden materials.

Coding

Coded - Design and coding required

Number of Pages Required

5+ page

Font styles to use
Serif

Colors
cadf82
abd037
9bcb3c
fee18a
ffcf3e
ffc214

Requirements
Must have
• The web will exist in three possible languages in czech, english and deutsch.
• First page : introduction of a company
• Second page : Area of expertise
• Third page: servicies our company provides
• Fourth page: Our partners
• Fifth page: Conditions of our servicies
• Sixth page: Succesful projects
• - we would also love if we had possibility to add videos about our successful projects
• Seventh: Our team
• We are serious company in the sphere of funds and counsilary servicies, that is why we would love to have web design as representative as possible
• Take on mind that that we are specializing on development management, try to apply that on your design
• In the section of contacts, we would love to have photos of our team,
• This is our current site: http://www.trnavska.eu/cz/partneri.html
• This is how our concurency sites are lookin. Take these designs as an slight inspiration.
• http://www.valbrinetica.sk/en/
• https://www2.quorvany.com/global/en.html
Nice to have
• Visible logo on the front page for the visitor.
• As a inspiration we provided link for our current web design, but we dont want to copy the current style, just look at the logo and the pages that exists on current web.
• !!!!!!We also uploaded file, where we explain how our cooperation with partner works. Especially in the part 2. section of service. Take that as an ispiration too, or use that to understand, what our company do.
Should not have
• We are serious company in the sphere of funds and counsilary servicies, that is why we would love to have web design representative as possible

```html
<!DOCTYPE html>
<html lang="en">
<head>
<meta charset="utf-8">
<title>1. Trnavska s.r.o. – Beratungsfirma</title>
<link rel="stylesheet" href="https://fonts.googleapis.com/css2?family=Montserrat:wght@800&family=Poppins:wght@300;400;600;700&display=swap">
<style>
  :root {
    --header-bg: #2a2a2a;
    --brand-green: #0a8c40;
    --accent-orange: #ffa500;
    --text-light: #ffffff;
    --hero-dark: #4c751f;
    --hero-mid: #78ab1c;
    --hero-light: #a8e028;
    --page-bg: #ffffff;
  }
  * { margin: 0; padding: 0; box-sizing: border-box; }
  html, body {
    width: 1200px;
    height: 548px;
    overflow: hidden;
    background: var(--page-bg);
    font-family: "Poppins", sans-serif;
  }
  .site-header {
    position: relative;
    height: 167px;
    background: var(--header-bg);
  }
  .brand-mark {
    position: absolute;
    left: 67px;
    top: 40px;
    width: 108px;
    height: 108px;
    background: var(--brand-green);
    border: 5px solid var(--text-light);
  }
  .brand-text {
    position: absolute;
    left: 242px;
    top: 60px;
  }
  .brand-name {
    font-family: "Montserrat", sans-serif;
    font-weight: 800;
    font-size: 30px;
    line-height: 32px;
    color: var(--brand-green);
  }
  .brand-tagline {
    margin-top: 3px;
    font-family: "Montserrat", sans-serif;
    font-weight: 800;
    font-size: 19px;
    line-height: 24px;
    color: var(--accent-orange);
  }
  .top-nav {
    position: absolute;
    right: 83px;
    top: 24px;
    display: flex;
    gap: 28px;
    font-size: 14px;
    color: var(--text-light);
  }
  .lang-switch {
    display: flex;
    align-items: center;
    gap: 12px;
  }
  .company-address {
    position: absolute;
    left: 927px;
    top: 74px;
    font-style: normal;
    font-weight: 600;
    font-size: 14px;
    line-height: 20px;
    color: var(--accent-orange);
  }
  .hero {
    position: relative;
    height: 333px;
    background:
      radial-gradient(ellipse 40% 75% at 28% 25%, var(--hero-dark) 0%, rgba(76,117,31,0.6) 45%, transparent 80%),
      radial-gradient(ellipse 35% 65% at 100% 20%, var(--hero-light) 0%, transparent 80%),
      linear-gradient(100deg, #84b22a 0%, #6e9a22 35%, var(--hero-mid) 65%, #8cc424 100%);
  }
  .hero-copy {
    position: absolute;
    left: 133px;
    top: 112px;
    color: var(--text-light);
  }
  .hero-heading {
    font-weight: 700;
    font-size: 52px;
    line-height: 1.2;
  }
  .hero-subheading {
    font-weight: 300;
    font-size: 43px;
    line-height: 1.2;
    margin-top: 8px;
  }
</style>
</head>
<body>
  <header class="site-header">
    <div class="brand-mark"></div>
    <div class="brand-text">
      <div class="brand-name">1. Trnavska s.r.o.</div>
      <div class="brand-tagline">Beratungsfirma</div>
    </div>
    <nav class="top-nav">
      <span class="lang-switch">English
        <svg width="11" height="8" viewBox="0 0 11 8" aria-hidden="true"><path d="M1.5 1.5 L5.5 5.5 L9.5 1.5" fill="none" stroke="#ffffff" stroke-width="2.2"/></svg>
      </span>
      <span class="nav-link">Contact</span>
    </nav>
    <address class="company-address">
      1. Trnavska s.r.o, ID 4719<br>
      Lindenweg 14<br>
      02790 Kestrow
    </address>
  </header>
  <section class="hero">
    <div class="hero-copy">
      <h1 class="hero-heading">Dont Find Solution!</h1>
      <p class="hero-subheading">We are here to help you.</p>
    </div>
  </section>
</body>
</html>
```